Washbag retail Packaging

We need a cardboard insert card design for a delicates washbag. The size for front panel would be 9cm wide and height 12cm, then a fold and the back panel would be the same size. This insert is packed into a clear hangsell polybag , and the white mesh washbag is folded up inside. We want to extend our brand using similar fonts , and colours - as shown in the photgraph, the PMS 241 is really our brand colour. But also introduce something appealing a beautiful about the washbag packaging. The washbag itself is a very plain and boring product. I have included an old artwork for the same product - the yellow box which does not suit the range at all. Please note the new packaging is not a box, but an insert card in a poly bag, and there will not be a window.
Updates

Target Market(s)

Mainly women all ages, Mid range supermarket, lingerie stores, hosiery and stockings stores

Industry/Entity Type

Retail

Font styles to use
Sans Serif

Colors
e667a6
faeaf3
eea4c8
b868aa

Requirements
Must have
• PMS 241 and work with other products in the range
Nice to have
• Something a little more pretty

```html
<!DOCTYPE html>
<html lang="en">
<head>
<meta charset="utf-8">
<title>Wash Bag Insert Card</title>
<link rel="stylesheet" href="https://fonts.googleapis.com/css2?family=Source+Sans+3:ital,wght@0,400;0,600;1,600;1,700&display=swap">
<style>
  :root {
    --stage: #e8e8e8;
    --card: #fae9f2;
    --brand-cyan: #3fc7e4;
    --brand-teal: #2ba6c2;
    --brand-navy: #26306a;
    --ink: #3a3a3a;
    --label: #555555;
    --pink-soft: #eea4c8;
    --pink: #e667a6;
    --mauve: #b868aa;
  }
  * { box-sizing: border-box; margin: 0; padding: 0; }
  html, body { width: 1200px; height: 818px; overflow: hidden; }
  body {
    background: var(--stage);
    font-family: "Source Sans 3", sans-serif;
    position: relative;
  }
  .panel-label {
    position: absolute;
    top: 14px;
    width: 546px;
    text-align: center;
    font-size: 58px;
    font-weight: 400;
    color: var(--label);
    line-height: 1;
  }
  .panel-label--front { left: 49px; }
  .panel-label--back { left: 610px; }

  .panel {
    position: absolute;
    top: 76px;
    width: 546px;
    height: 728px;
    background: var(--card);
    overflow: hidden;
  }
  .panel--front { left: 49px; }
  .panel--back { left: 610px; }

  .line-swirl {
    position: absolute;
    top: 0;
    right: 0;
    width: 300px;
    height: 728px;
    background: linear-gradient(200deg, rgba(238,164,200,0.35), rgba(230,103,166,0.15) 50%, rgba(250,233,242,0) 80%);
  }
  .peony {
    position: absolute;
    left: 0;
    bottom: 0;
    width: 220px;
    height: 180px;
    border-top-right-radius: 60% 55%;
    background: radial-gradient(circle at 38% 60%, #f7c0d6 0%, var(--pink) 45%, #f08aa8 70%, rgba(156,176,74,0.55) 100%);
  }
  .panel--back .peony { width: 190px; height: 150px; }
  .streamers {
    position: absolute;
    right: 0;
    bottom: 0;
    width: 160px;
    height: 130px;
    background: linear-gradient(315deg, rgba(240,150,130,0.55), rgba(250,233,242,0));
  }
  .plume {
    position: absolute;
    left: 0;
    top: 0;
    width: 120px;
    height: 165px;
    border-bottom-right-radius: 70% 60%;
    background: linear-gradient(160deg, var(--mauve), var(--pink) 60%, rgba(250,233,242,0));
  }

  .brand-name {
    position: absolute;
    left: 40px;
    top: 58px;
    font-size: 40px;
    font-weight: 600;
    color: var(--brand-navy);
    letter-spacing: 0.5px;
  }
  .product-title {
    position: absolute;
    left: 0;
    width: 100%;
    text-align: center;
    font-weight: 400;
    color: var(--brand-cyan);
    line-height: 1;
    letter-spacing: -1px;
  }
  .panel--front .product-title { top: 168px; font-size: 100px; }
  .panel--back .product-title { top: 80px; left: 30px; font-size: 70px; }
  .product-sub {
    position: absolute;
    top: 274px;
    width: 100%;
    text-align: center;
    font-size: 42px;
    color: var(--brand-teal);
    line-height: 1;
  }
  .tagline {
    position: absolute;
    top: 378px;
    left: 0;
    width: 100%;
    text-align: center;
    font-size: 42px;
    font-style: italic;
    font-weight: 600;
    line-height: 52px;
    color: var(--ink);
    text-shadow: 0 0 3px #fff, 0 0 3px #fff, 2px 2px 2px rgba(0,0,0,0.2);
  }

  .care-copy {
    position: absolute;
    top: 172px;
    left: 0;
    width: 100%;
    text-align: center;
    font-size: 16.5px;
    line-height: 20.4px;
    color: var(--ink);
  }
  .care-copy h2 {
    font-size: 18px;
    font-style: italic;
    font-weight: 700;
    color: var(--label);
    line-height: 22px;
  }
  .spec {
    position: absolute;
    top: 642px;
    width: 100%;
    text-align: center;
    font-size: 13.5px;
    line-height: 18px;
    color: var(--ink);
  }
</style>
</head>
<body>
  <h1 class="panel-label panel-label--front">Front</h1>
  <h1 class="panel-label panel-label--back">Back</h1>

  <section class="panel panel--front">
    <div class="line-swirl" role="img" aria-label="Fine pink flowing line pattern"></div>
    <div class="streamers" role="img" aria-label="Coral ribbon streamers illustration"></div>
    <div class="peony" role="img" aria-label="Pink peony flower illustration"></div>
    <p class="brand-name">bellmere</p>
    <h2 class="product-title">Wash Bag</h2>
    <p class="product-sub">For Delicates</p>
    <p class="tagline">Protects delicate items<br>from tangles and snags<br>in the wash and dryer</p>
  </section>

  <section class="panel panel--back">
    <div class="line-swirl" role="img" aria-label="Fine pink flowing line pattern"></div>
    <div class="streamers" role="img" aria-label="Coral ribbon streamers illustration"></div>
    <div class="peony" role="img" aria-label="Pink peony flower illustration"></div>
    <div class="plume" role="img" aria-label="Purple and pink feather plume ornament"></div>
    <h2 class="product-title">Wash Bag</h2>
    <div class="care-copy">
      <h2>Delicates and hoisery</h2>
      <p>Protects small and delicate items from tangles and snags<br>
      A safe and convenient way to machine wash and dry<br>
      your delicates, such as hosiery, underwear ,<br>
      delicates and baby clothes. They are protected from<br>
      snaring and tangling, even in the largest of loads.</p>
      <h2>Directions.</h2>
      <p>Please observe the garment manufacturers<br>
      care instructions before proceeding.<br>
      Place your delicates inside the bag, fasten<br>
      the zip, and place in the washing machine.<br>
      The fine mesh will allow water and detergent<br>
      to circulate evenly amongst the garments.<br>
      The washbag may be placed directly into<br>
      the clothes dryer if appropriate for your garment.<br>
      The washbag can also be used to protect and isolate<br>
      your delicates in your luggage when travelling.<br>
      Bellmere Products . Vic. 3000.<br>
      Bag made in China, printed and packed in Australia.100% polyester</p>
    </div>
    <p class="spec">30cm x 40cm<br>Freeflow mesh with contrast zip</p>
  </section>
</body>
</html>
```